Psychology practice - information brochure/flyer - half A4 page folded (4 sides)

We need a brochure/flyer to market our psychology service to GPs (Doctors). We need to demonstrate to the doctors that we are the right choice for their patients, and that we cover a large range of services so all of their patients needs are met. We will demonstrate this by listing our range of services and our team of psychologists. We have two locations in Sydney and offer high end services. I've attached our company logo but we remain flexible regarding the style of the brochures. I will provide more details (services, locations & psychologist credentials) once our preferred brochure design has been selected.

```html
<!DOCTYPE html>
<html lang="en">
<head>
<meta charset="utf-8">
<title>Bright Mind Clinical Psychology – Brochure</title>
<link rel="stylesheet" href="https://fonts.googleapis.com/css2?family=Open+Sans:ital,wght@0,400;0,600;0,700;1,400&display=swap">
<style>
:root{
  --gold:#f5b800;
  --gold-deep:#e2a300;
  --gold-pale:#fbe5a0;
  --charcoal:#4a4a4d;
  --ink:#3e3e3e;
  --pill-text:#5a3a00;
  --white:#ffffff;
  --table-bg:#ececec;
  --table-cell:#f7f7f7;
  --page-bg:#e9e7e4;
}
*{margin:0;padding:0;box-sizing:border-box}
html,body{width:866px;height:1200px;overflow:hidden;background:var(--page-bg)}
body{position:relative;font-family:"Open Sans",Arial,sans-serif;color:var(--ink)}
.spread{position:absolute;left:23px;width:953px;height:675px;transform:scale(.86);transform-origin:0 0;overflow:hidden;background:var(--white);box-shadow:0 3px 10px rgba(0,0,0,.18)}
.spread--cover{top:12px}
.spread--inside{top:607px}
.spread svg.shapes{position:absolute;left:0;top:0}
.abs{position:absolute}
.fold{position:absolute;left:476px;top:0;width:2px;height:100%;background:rgba(0,0,0,.06)}

/* brand */
.brand{position:absolute;display:flex;align-items:center;gap:10px;color:var(--charcoal);font-weight:400;line-height:1.05}
.brand__dot{width:12px;height:12px;background:var(--gold);border-radius:50%;flex:none}
.brand--cover{left:510px;top:58px;font-size:34px}
.brand--back{left:173px;top:580px;font-size:19px;color:var(--white)}
.brand--back .brand__dot{width:8px;height:8px}
.new-location{position:absolute;left:185px;top:635px;width:125px;font-size:7px;color:var(--white);text-align:center;border-top:1px solid rgba(255,255,255,.5);border-bottom:1px solid rgba(255,255,255,.5);padding:3px 0}

/* cover contact */
.contact-title{left:41px;top:298px;color:var(--white);font-weight:700;font-size:11px;line-height:1.3}
.contact-list{position:absolute;left:20px;top:336px;list-style:none;color:var(--white);font-size:10.5px}
.contact-list li{display:flex;gap:8px;align-items:flex-start;margin-bottom:8px;line-height:1.3}
.contact-list svg{flex:none;margin-top:1px}
.contact-list .small{font-size:8.5px}

.headline{color:var(--white);font-weight:700;text-transform:uppercase;line-height:1.35;letter-spacing:.3px;text-shadow:0 1px 3px rgba(0,0,0,.25)}
.headline .accent{color:var(--gold-pale)}
.headline--cover{left:516px;top:248px;font-size:24px}
.headline--inside{right:53px;top:38px;font-size:24px;text-align:right}
.web{display:flex;align-items:center;gap:8px;color:var(--white);font-size:11px;letter-spacing:.3px}
.web--cover{left:622px;top:625px}
.web--inside{left:700px;top:645px}

/* inside */
.pill{position:absolute;height:24px;border-radius:12px;background:var(--gold);color:var(--pill-text);font-weight:700;font-size:12.5px;line-height:24px;padding:0 13px;box-shadow:0 2px 3px rgba(0,0,0,.2);white-space:nowrap}
.bullets{position:absolute;list-style:none;font-size:10.3px;color:var(--ink)}
.bullets li{position:relative;padding-left:17px;height:16.36px;line-height:16.36px}
.bullets li::before{content:"";position:absolute;left:0;top:6px;width:5px;height:5px;border-radius:50%;background:var(--gold)}
.bullets li.wrap{height:31.5px;line-height:15.7px}
.services{left:48px;top:276px}
.groups{left:321px;top:276px}
.hours{left:316px;top:474px;font-size:10.3px;line-height:18px}
.hours b{font-weight:700}
.clinicians{position:absolute;left:512px;top:280px;list-style:none}
.clinicians li{position:absolute;left:0;display:flex;gap:6px;white-space:nowrap}
.clinicians .tick{width:7px;height:12px;flex:none}
.clinicians .name{font-weight:700;font-size:10.5px;color:var(--ink)}
.clinicians .cred{font-size:6.6px;color:#666;line-height:1.45}

.fees{position:absolute;left:500px;top:478px;width:432px;border-collapse:collapse;font-size:10px;background:var(--table-bg)}
.fees td{height:19.5px;padding:0 6px;border-bottom:1px solid var(--white);white-space:nowrap}
.fees .band td{background:var(--gold);color:var(--pill-text);font-weight:700;font-size:9px;text-align:center;height:18px}
.fees .price{font-weight:700;width:43px}
.fees .per,.fees .rebate{font-style:italic}
.fees .kind{font-weight:700;font-size:9.5px}
.fees .amount{font-weight:700;background:var(--table-cell);text-align:right}
.fees tr.gap td{height:4px;padding:0;background:var(--table-bg)}
</style>
</head>
<body>

<!-- Cover spread: back panel (left) and front panel (right) -->
<section class="spread spread--cover">
  <svg class="shapes" width="953" height="675" viewBox="0 0 953 675">
    <defs>
      <linearGradient id="fieldGrad" x1="0" y1="0" x2="0.4" y2="1">
        <stop offset="0" stop-color="#f6e27a"/>
        <stop offset="0.35" stop-color="#d5bf4e"/>
        <stop offset="0.7" stop-color="#8fa53a"/>
        <stop offset="1" stop-color="#6d8a2c"/>
      </linearGradient>
      <radialGradient id="sunGlow" cx="0.62" cy="0.45" r="0.45">
        <stop offset="0" stop-color="#fffbe0"/>
        <stop offset="1" stop-color="#fffbe0" stop-opacity="0"/>
      </radialGradient>
      <radialGradient id="flowerGrad" cx="0.15" cy="0.35" r="0.8">
        <stop offset="0" stop-color="#7a4a12"/>
        <stop offset="0.25" stop-color="#f3b410"/>
        <stop offset="0.7" stop-color="#f7d23a"/>
        <stop offset="1" stop-color="#fff3c0"/>
      </radialGradient>
      <linearGradient id="panelGrad" x1="0" y1="0" x2="0" y2="1">
        <stop offset="0" stop-color="#f8c623"/>
        <stop offset="1" stop-color="#e6a90a"/>
      </linearGradient>
    </defs>
    <rect x="0" y="0" width="953" height="675" fill="url(#fieldGrad)" role="img" aria-label="Photo: young woman sitting cross-legged in a sunlit meadow, smiling upward"/>
    <rect x="292" y="120" width="661" height="460" fill="url(#sunGlow)"/>
    <path d="M0,0 H953 V100 C860,145 760,158 620,165 C480,172 380,170 292,183 C180,200 80,235 0,265 Z" fill="var(--white)"/>
    <path d="M0,0 H300 C260,80 200,150 160,212 C100,228 50,248 0,265 Z" fill="url(#flowerGrad)" role="img" aria-label="Photo: close-up of a sunflower"/>
    <path d="M0,268 C80,238 180,203 292,186 V560 C180,565 80,585 0,600 Z" fill="url(#panelGrad)"/>
    <path d="M0,265 C80,235 180,200 292,183 C380,170 480,172 620,165 C760,158 860,145 953,100" fill="none" stroke="var(--gold)" stroke-width="6"/>
    <path d="M0,258 C80,228 180,194 292,177 C380,164 480,166 620,159 C760,152 860,139 953,94" fill="none" stroke="var(--white)" stroke-width="2"/>
    <path d="M0,575 C200,520 420,515 620,548 C760,570 860,590 953,572 V675 H0 Z" fill="var(--gold)"/>
    <path d="M0,590 C200,538 420,535 620,565 C760,585 860,600 953,585 V675 H0 Z" fill="var(--white)"/>
    <path d="M0,596 C200,545 420,542 620,572 C760,592 860,607 953,592 V675 H0 Z" fill="var(--charcoal)"/>
  </svg>
  <div class="fold"></div>

  <p class="abs contact-title">To Make Appointments<br>Please Contact us on below</p>
  <ul class="contact-list">
    <li><svg width="12" height="13" viewBox="0 0 12 13"><rect x="3" y="1" width="6" height="11" rx="1.5" fill="none" stroke="#fff" stroke-width="1.3"/></svg>(02) 5550 1234</li>
    <li><svg width="12" height="13" viewBox="0 0 12 13"><rect x="3" y="1" width="6" height="4" fill="none" stroke="#fff" stroke-width="1.2"/><rect x="1" y="5" width="10" height="5" rx="1" fill="none" stroke="#fff" stroke-width="1.2"/><rect x="3" y="8" width="6" height="4" fill="#fff"/></svg>(02) 5550 5678</li>
    <li><svg width="12" height="13" viewBox="0 0 12 13"><path d="M6,12 C2,7 2,5.5 2,4.5 A4,4 0 0 1 10,4.5 C10,5.5 10,7 6,12 Z" fill="none" stroke="#fff" stroke-width="1.3"/><circle cx="6" cy="4.6" r="1.4" fill="#fff"/></svg>Suite 2, Level 1, 14 Harbour Lane<br>Riverton NSW 2199</li>
    <li><svg width="12" height="13" viewBox="0 0 12 13"><path d="M6,12 C2,7 2,5.5 2,4.5 A4,4 0 0 1 10,4.5 C10,5.5 10,7 6,12 Z" fill="none" stroke="#fff" stroke-width="1.3"/><circle cx="6" cy="4.6" r="1.4" fill="#fff"/></svg>Shop 8, 42 Maple St, Westbrook NSW 2050</li>
    <li><svg width="12" height="13" viewBox="0 0 12 13"><circle cx="6" cy="6.5" r="5" fill="none" stroke="#fff" stroke-width="1.2"/><ellipse cx="6" cy="6.5" rx="2.2" ry="5" fill="none" stroke="#fff" stroke-width="1"/><line x1="1" y1="6.5" x2="11" y2="6.5" stroke="#fff"/></svg>www.brightmindpsychology.com.au</li>
    <li class="small"><svg width="12" height="10" viewBox="0 0 12 10"><rect x="1" y="1.5" width="10" height="7" fill="none" stroke="#fff" stroke-width="1.1"/><path d="M1,1.5 L6,5.5 L11,1.5" fill="none" stroke="#fff" stroke-width="1.1"/></svg>info@brightmindpsychology.com.au</li>
  </ul>

  <div class="brand brand--back"><span class="brand__dot"></span><span>Bright Mind<br>Clinical Psychology</span></div>
  <p class="new-location">New location in Maple St Westbrook</p>

  <div class="brand brand--cover"><span class="brand__dot"></span><span>Bright Mind<br>Clinical Psychology</span></div>
  <h1 class="abs headline headline--cover">Working together<br>to achieve a <span class="accent">better</span><br><span class="accent">quality of life</span></h1>
  <p class="abs web web--cover"><svg width="13" height="13" viewBox="0 0 12 13"><circle cx="6" cy="6.5" r="5" fill="none" stroke="#fff" stroke-width="1.2"/><ellipse cx="6" cy="6.5" rx="2.2" ry="5" fill="none" stroke="#fff" stroke-width="1"/><line x1="1" y1="6.5" x2="11" y2="6.5" stroke="#fff"/></svg>www.brightmindpsychology.com.au</p>
</section>

<!-- Inside spread -->
<section class="spread spread--inside">
  <svg class="shapes" width="953" height="675" viewBox="0 0 953 675">
    <defs>
      <linearGradient id="grassGrad" x1="0" y1="0" x2="1" y2="1">
        <stop offset="0" stop-color="#4f8a2c"/>
        <stop offset="0.5" stop-color="#3f7424"/>
        <stop offset="1" stop-color="#2f5e1c"/>
      </linearGradient>
      <radialGradient id="manGrad" cx="0.5" cy="0.5" r="0.5">
        <stop offset="0" stop-color="#efeee6"/>
        <stop offset="0.6" stop-color="#c9c8b8"/>
        <stop offset="1" stop-color="#c9c8b8" stop-opacity="0"/>
      </radialGradient>
      <radialGradient id="softPhoto" cx="0.5" cy="0.5" r="0.55">
        <stop offset="0" stop-color="#cfd6dc"/>
        <stop offset="0.6" stop-color="#e4e8eb"/>
        <stop offset="1" stop-color="#ffffff" stop-opacity="0"/>
      </radialGradient>
      <radialGradient id="warmPhoto" cx="0.5" cy="0.5" r="0.55">
        <stop offset="0" stop-color="#d8cbbd"/>
        <stop offset="0.6" stop-color="#ebe4dc"/>
        <stop offset="1" stop-color="#ffffff" stop-opacity="0"/>
      </radialGradient>
    </defs>
    <rect x="0" y="0" width="953" height="235" fill="url(#grassGrad)" role="img" aria-label="Photo: young man lying on the grass with hands behind his head, smiling"/>
    <ellipse cx="230" cy="105" rx="190" ry="110" fill="url(#manGrad)"/>
    <path d="M0,98 C80,150 200,195 400,192 C560,190 700,168 820,178 C880,183 920,200 953,220 V675 H0 Z" fill="var(--gold)"/>
    <path d="M0,110 C80,160 200,203 400,200 C560,198 700,176 820,186 C880,191 920,208 953,228 V675 H0 Z" fill="var(--white)"/>
    <rect x="150" y="330" width="190" height="112" fill="url(#softPhoto)" role="img" aria-label="Photo: carer holding hands with an elderly woman"/>
    <rect x="255" y="505" width="235" height="160" fill="url(#warmPhoto)" role="img" aria-label="Photo: couple in a counselling session with a therapist"/>
    <rect x="650" y="238" width="303" height="225" fill="url(#softPhoto)" role="img" aria-label="Photo: psychologist talking with a client on a sofa"/>
    <path d="M560,675 C700,640 820,620 953,618 V675 Z" fill="var(--gold)"/>
    <path d="M590,675 C720,648 830,632 953,632 V675 Z" fill="var(--charcoal)"/>
  </svg>
  <div class="fold"></div>

  <h2 class="abs headline headline--inside">We’re here to help<br>you get the <span class="accent">positive change</span><br>you’re looking for</h2>

  <h3 class="pill" style="left:32px;top:240px">Type of Services we provide:</h3>
  <ul class="bullets services">
    <li>Anxiety</li><li>Depression</li><li>Phobias</li><li>Intellectual disability</li><li>Learning difficulties</li><li>Bullying</li><li>Study stress</li><li>Procrastination</li><li>WorkCover</li><li>Stress management</li><li>Rehabilitation psychology</li><li>Addiction and relapse prevention</li><li>Attention Deficit Hyperactivity Disorder (ADHD)</li><li>Anger management</li><li>Divorce/separation</li><li>Pregnancy</li><li>Post-Traumatic Stress Disorder (PTSD)</li><li>Couples/Family Therapy</li><li>Domestic Violence</li><li>Non-Suicidal Self-Harm</li><li>Grief and loss</li><li>Eating disorders/body image</li><li>Trauma</li>
  </ul>

  <h3 class="pill" style="left:305px;top:242px">Our Client Groups:</h3>
  <ul class="bullets groups">
    <li>Children 5-12</li><li>Adolescents</li><li>Adults</li><li>Veterans</li><li>Victims of crime</li><li>Injured workers</li><li class="wrap">Culturally and Linguistically<br>Diverse backgrounds</li><li>Refugees</li>
  </ul>

  <h3 class="pill" style="left:305px;top:440px">Hours of Operation</h3>
  <p class="abs hours"><b>Monday – Friday :</b>&nbsp; 8am-6pm<br><b>Saturday :</b>&nbsp; 9am – 1pm</p>

  <h3 class="pill" style="left:496px;top:242px;padding:0 21px">Our Clinicians</h3>
  <ul class="clinicians">
    <li style="top:0"><svg class="tick" viewBox="0 0 7 12"><path d="M1,7 L3,11 L6,1" fill="none" stroke="var(--gold)" stroke-width="1.6"/></svg><div><p class="name">Dr Helen Marsh</p><p class="cred">DClinPsych, MA, BSc(Psych), BPsych (Hons)</p></div></li>
    <li style="top:37px"><svg class="tick" viewBox="0 0 7 12"><path d="M1,7 L3,11 L6,1" fill="none" stroke="var(--gold)" stroke-width="1.6"/></svg><div><p class="name">Dr Thomas Alan Reid</p><p class="cred">DPhil (Psych), BA-Psych (Hons),<br>GradDipEd, GDipMgt, MAPS, FCCP</p></div></li>
    <li style="top:81px"><svg class="tick" viewBox="0 0 7 12"><path d="M1,7 L3,11 L6,1" fill="none" stroke="var(--gold)" stroke-width="1.6"/></svg><div><p class="name">Sarah Kellerman</p><p class="cred">MPsych (Clin), BPsych (Hons)</p></div></li>
    <li style="top:112px"><svg class="tick" viewBox="0 0 7 12"><path d="M1,7 L3,11 L6,1" fill="none" stroke="var(--gold)" stroke-width="1.6"/></svg><div><p class="name">Dr Nadia Costa</p><p class="cred">D ClinPsych, MSc (Psych), B Psych (Hons),<br>MACPA, MAPS</p></div></li>
  </ul>

  <h3 class="pill" style="left:496px;top:442px;padding:0 21px">Our Fee Structure</h3>
  <table class="fees">
    <tr class="band"><td colspan="5">BusinessHours – 9am to 5pm</td></tr>
    <tr><td class="price">$150</td><td class="per">per session for</td><td class="kind">General Psychologist,</td><td class="rebate">with Medicare Rebate of</td><td class="amount">$84.80</td></tr>
    <tr><td class="price">$190</td><td class="per">per session for</td><td class="kind">Clinical Psychologist,</td><td class="rebate">with Medicare Rebate of</td><td class="amount">$124.50</td></tr>
    <tr class="band"><td colspan="5">Out of Hours – weekends and after 5pm</td></tr>
    <tr class="gap"><td colspan="5"></td></tr>
    <tr><td class="price">$170</td><td class="per">per session for</td><td class="kind">General Psychologist,</td><td class="rebate">with Medicare Rebate of</td><td class="amount">$84.80</td></tr>
    <tr><td class="price">$210</td><td class="per">per session for</td><td class="kind">Clinical Psychologist,</td><td class="rebate">with Medicare Rebate of</td><td class="amount">$124.50</td></tr>
  </table>

  <p class="abs web web--inside"><svg width="13" height="13" viewBox="0 0 12 13"><circle cx="6" cy="6.5" r="5" fill="none" stroke="#fff" stroke-width="1.2"/><ellipse cx="6" cy="6.5" rx="2.2" ry="5" fill="none" stroke="#fff" stroke-width="1"/><line x1="1" y1="6.5" x2="11" y2="6.5" stroke="#fff"/></svg>www.brightmindpsychology.com.au</p>
</section>

</body>
</html>
```